LOS PINOS DE ARENA - EXCLUSIVE AND LUXURY REAL ESTATE PROJECT

Se trata del diseño de un mono poste grande (4 m x 2 m) o (8m x 3m) anunciando la construcción de 30 villas de lujo en un terreno en primera línea de playa en el sur de España (Cádiz).

La idea es crear expectación y transmitir lujo y exclusividad.

Target Market(s)

Clientes de alto poder adquisitivo que quieran adquirir su segunda vivienda en un entorno privilegiado a escasos pasos de una de las playas más bonitas de Cádiz.

Industry/Entity Type

REAL ESTATE

Colors

Designer to choose colors to be used in the design.

Requirements
Must have
• LOS PINOS DE ARENA as the name of the development
Nice to have
• Crear expectación con ideas del tipo: “Coming soon” o “No te lo puedes perder”

```html
<!DOCTYPE html>
<html lang="en">
<head>
<meta charset="utf-8">
<title>Los Pinos de Arena – Coming Soon Billboard</title>
<link rel="stylesheet" href="https://fonts.googleapis.com/css2?family=Oswald:wght@400;500;700&family=Yellowtail&family=Damion&display=swap">
<style>
  :root {
    --page: #e8e4e3;
    --navy: #0a1729;
    --cyan: #62f0ff;
    --white: #ffffff;
    --sky: #3a6fd6;
    --haze: #d7dde3;
    --deck: #7d5236;
  }
  * { margin: 0; padding: 0; box-sizing: border-box; }
  html, body {
    width: 960px;
    height: 1200px;
    overflow: hidden;
    background: var(--page);
  }
  .billboard {
    position: absolute;
    left: 40px;
    top: 380px;
    width: 880px;
    height: 440px;
    overflow: hidden;
    box-shadow: 0 4px 10px rgba(0, 0, 0, 0.35);
  }
  .villa-photo {
    position: absolute;
    inset: 0;
    background: linear-gradient(180deg, var(--sky) 0%, #6f9ae0 22%, var(--haze) 48%, #bfb8ae 62%, var(--deck) 80%, #5e3d29 100%);
  }
  .board-shapes {
    position: absolute;
    inset: 0;
    width: 880px;
    height: 440px;
  }
  .development-name {
    position: absolute;
    right: 40px;
    top: 22px;
    font-family: "Oswald", sans-serif;
    font-weight: 400;
    font-size: 92px;
    line-height: 96px;
    color: var(--cyan);
    text-align: right;
    text-transform: uppercase;
  }
  .tagline {
    position: absolute;
    right: 40px;
    top: 262px;
    font-family: "Damion", cursive;
    font-size: 42px;
    line-height: 50px;
    color: var(--navy);
  }
  .coming {
    position: absolute;
    left: 60px;
    top: 276px;
    font-family: "Oswald", sans-serif;
    font-weight: 700;
    font-size: 96px;
    line-height: 110px;
    color: var(--white);
    text-transform: uppercase;
    text-shadow: -6px 2px 0 var(--navy);
  }
  .soon {
    position: absolute;
    left: 118px;
    top: 340px;
    font-family: "Yellowtail", cursive;
    font-size: 80px;
    line-height: 90px;
    color: var(--cyan);
    -webkit-text-stroke: 2px var(--navy);
    transform: rotate(-8deg);
    transform-origin: left center;
  }
</style>
</head>
<body>
  <section class="billboard">
    <div class="villa-photo" role="img" aria-label="Photograph of a modern white luxury villa with a pool and wooden deck under a blue sky"></div>

    <svg class="board-shapes" viewBox="0 0 880 440" aria-hidden="true">
      <defs>
        <clipPath id="panel-clip">
          <polygon points="338,0 880,0 880,440 520,440"/>
        </clipPath>
      </defs>
      <polygon class="accent-stripe" points="326,0 338,0 520,440 508,440" fill="var(--cyan)"/>
      <polygon class="name-panel" points="338,0 880,0 880,440 520,440" fill="var(--navy)"/>
      <g clip-path="url(#panel-clip)">
        <path class="wave-band" d="M400,262 C460,248 500,250 560,262 C620,274 660,246 720,258 C780,270 830,250 880,256 L880,368 C830,364 800,380 760,376 C720,372 690,362 640,368 C590,374 560,382 520,378 C480,374 440,372 400,374 Z" fill="var(--cyan)"/>
        <path class="wave-line" d="M400,384 C440,378 480,382 520,388 C560,394 590,386 640,378 C690,370 720,384 760,386 C800,388 830,374 880,376" fill="none" stroke="var(--white)" stroke-width="8"/>
      </g>
    </svg>

    <h1 class="development-name">Los Pinos<br>De Arena</h1>
    <p class="tagline">You can't Miss it</p>
    <p class="coming">Coming</p>
    <p class="soon">Soon!</p>
  </section>
</body>
</html>
```